Dental specialist needs a sharp looking letterhead

I am looking for a letterhead to be used to send letters and communication between myself (a dental specialist) and other dentists.
My office is a state of the art dental specialty office.
I need to letterhead to also state:
Gideon R. Whitfield DDS
2847 Birchmont Avenue, Suite K
West Harlow, NY 14391
(716)482-9163
fax: (716)482-9170
whitfieldroot.com (**this email address may change)

i included my logo designs.
thank you

Target Market(s)

dentists

Industry/Entity Type

Communication

Requirements
Must have
• the included logo, whether the vertical or horizontal versions

```html
<!DOCTYPE html>
<html lang="en">
<head>
<meta charset="utf-8">
<title>Keystone Endodontics – Letterhead</title>
<link rel="stylesheet" href="https://fonts.googleapis.com/css2?family=Open+Sans:wght@400;600;700&display=swap">
<style>
  :root {
    --backdrop: #8e8e8e;
    --paper: #ffffff;
    --ink: #3a3a3a;
    --ink-soft: #555555;
    --brand-blue: #29a9e1;
    --brand-green: #8dc63f;
  }
  html, body {
    margin: 0;
    padding: 0;
    width: 1200px;
    height: 916px;
    overflow: hidden;
    background: var(--backdrop);
    font-family: "Open Sans", Arial, sans-serif;
  }
  .letterhead {
    position: absolute;
    left: 290px;
    top: 40px;
    width: 620px;
    height: 836px;
    background: var(--paper);
    box-shadow: 0 6px 24px rgba(0,0,0,0.25);
    color: var(--ink);
  }
  .masthead {
    position: absolute;
    left: 44px;
    top: 44px;
    width: 210px;
  }
  .brand {
    display: flex;
    align-items: center;
    gap: 8px;
  }
  .brand-dot {
    width: 22px;
    height: 22px;
    border-radius: 50%;
    background: var(--brand-blue);
    flex: none;
  }
  .brand-name {
    font-size: 13px;
    font-weight: 700;
    color: var(--ink);
    line-height: 1.15;
    letter-spacing: 0.5px;
  }
  .doctor {
    margin-top: 8px;
    text-align: right;
    font-size: 12px;
    letter-spacing: 1.2px;
    color: var(--brand-blue);
  }
  .doctor-credential {
    display: block;
    font-size: 10px;
    color: var(--brand-green);
    letter-spacing: 1px;
  }
  .contact {
    margin-top: 12px;
    text-align: right;
    font-size: 9.5px;
    line-height: 1.55;
    color: var(--ink);
  }
  .contact-label { color: var(--brand-blue); }
  .letter {
    position: absolute;
    left: 210px;
    top: 250px;
    width: 370px;
    font-size: 8.5px;
    line-height: 1.45;
    color: var(--ink-soft);
  }
  .letter p { margin: 0 0 10px; }
  .letter .greeting { margin-bottom: 8px; }
  .letter .closing { margin-top: 70px; padding-left: 90px; }
  .footer-web {
    position: absolute;
    left: 0;
    right: 0;
    bottom: 40px;
    text-align: center;
    font-size: 12px;
    letter-spacing: 5px;
    color: var(--brand-blue);
  }
</style>
</head>
<body>
  <main class="letterhead">
    <header class="masthead">
      <div class="brand">
        <span class="brand-dot"></span>
        <span class="brand-name">Keystone Endodontics P.C.</span>
      </div>
      <div class="doctor">
        Gideon R. Whitfield
        <span class="doctor-credential">D.D.S</span>
      </div>
      <address class="contact" style="font-style:normal">
        <span class="contact-label">Address:</span> 2847 Birchmont Avenue<br>
        Suite K West Harlow, NY 14391<br>
        <span class="contact-label">Phone:</span> (716)482-9163<br>
        <span class="contact-label">Fax:</span> (716)482-9170
      </address>
    </header>

    <section class="letter">
      <p class="greeting">Lorem Ipsum,</p>
      <p>Lorem ipsum dolor sit amet, consectetuer adipiscing elit. Nam cursus. Morbi ut mi. Nullam enim leo, egestas id, condimentum at, laoreet mattis, massa. Sed eleifend nonummy diam. Praesent mauris ante, elementum et, bibendum at, posuere sit amet, nibh. Duis tincidunt lectus quis dui viverra vestibulum. Suspendisse vulputate aliquam dui. Nulla elementum dui ut augue.</p>
      <p>Aliquam vehicula mi at mauris. Maecenas placerat, nisl at consequat rhoncus, sem nunc gravida justo, quis eleifend arcu velit quis lacus. Morbi magna magna, tincidunt a, mattis non, imperdiet vitae, tellus.</p>
      <p>Mauris nunc quam, venenatis nec, euismod sit amet, egestas placerat, est. Pellentesque habitant morbi tristique senectus et netus et malesuada fames ac turpis egestas. Cras id elit. Integer quis urna.</p>
      <p>Aliquam vehicula mi at mauris. Maecenas placerat, nisl at consequat rhoncus, sem nunc gravida justo, quis eleifend arcu velit quis lacus. Morbi magna magna, tincidunt a, mattis non, imperdiet vitae, tellus.</p>
      <p>Mauris nunc quam, venenatis nec, euismod sit amet, egestas placerat, est. Pellentesque habitant morbi tristique senectus et netus et malesuada fames ac turpis egestas. Cras id elit. Integer quis urna.</p>
      <p class="closing">Sincerly,</p>
    </section>

    <footer class="footer-web">www.whitfieldroot.com</footer>
  </main>
</body>
</html>
```